New Web Design Project

Number of Pages Required

1 page

Requirements
Must have
• An Overview / Background of the Business & Services(not for profit rescue animal farm)
• The Target Market / Audience you are trying to reach (animal lovers)
• Design Specifics; any preferences or ideas for Style, Colour, Imagery, etc (no preferences)

```html
<!DOCTYPE html>
<html lang="en">
<head>
<meta charset="utf-8">
<title>Animal Sanctuary</title>
<link rel="stylesheet" href="https://fonts.googleapis.com/css2?family=Lato:wght@400;700;900&family=Raleway:wght@300;400;600&display=swap">
<style>
  :root {
    --green: #27a85a;
    --green-band: rgba(46, 170, 95, 0.92);
    --ink: #333333;
    --body-ink: #3d3d3d;
    --white: #ffffff;
    --blush: #f5f0f0;
  }
  * { box-sizing: border-box; margin: 0; padding: 0; }
  html, body { width: 960px; height: 1200px; overflow: hidden; background: var(--white); }
  body { position: relative; font-family: "Lato", sans-serif; color: var(--ink); }

  .site-header { position: absolute; left: 0; top: 0; width: 960px; height: 56px; background: var(--white); }
  .brand { position: absolute; left: 40px; top: 12px; display: flex; align-items: center; gap: 8px; }
  .brand-dot { width: 32px; height: 32px; border-radius: 50%; background: var(--green); }
  .brand-name { font-family: "Lato", sans-serif; font-weight: 900; font-size: 17px; color: var(--ink); }
  .main-nav { position: absolute; right: 40px; top: 19px; display: flex; gap: 25px; font-size: 13px; }
  .main-nav a { color: var(--ink); text-decoration: none; }
  .main-nav a.is-active { color: var(--green); }

  .hero { position: absolute; left: 0; top: 56px; width: 960px; height: 320px;
    background: linear-gradient(180deg, #2f4a22 0%, #4f7a2e 35%, #7fb84a 65%, #5e8c34 100%); }
  .hero-title { position: absolute; left: 0; width: 960px; top: 86px; text-align: center;
    font-weight: 900; font-size: 50px; color: var(--white); letter-spacing: -0.5px; }
  .hero-button { position: absolute; left: 404px; top: 167px; width: 152px; height: 40px;
    background: var(--green); color: var(--white); font-weight: 700; font-size: 14px;
    display: flex; align-items: center; justify-content: center; text-decoration: none; }

  .vision { position: absolute; left: 0; top: 376px; width: 960px; height: 280px; background: var(--white); }
  .section-title { font-family: "Raleway", sans-serif; font-weight: 600; font-size: 29px; color: var(--green); }
  .vision .section-title { position: absolute; left: 133px; top: 38px; }
  .vision-text { position: absolute; left: 133px; top: 106px; width: 436px;
    font-family: "Raleway", sans-serif; font-weight: 300; font-size: 12.8px; line-height: 22.4px; color: var(--body-ink); }
  .vision-photo { position: absolute; left: 576px; top: 0; width: 384px; height: 280px;
    background: linear-gradient(100deg, #ffffff 0%, #ece4dc 25%, #d8c8b8 55%, #8a6e5a 85%, #5a4436 100%); }

  .protection { position: absolute; left: 0; top: 656px; width: 960px; height: 544px; background: var(--blush); }
  .protection .section-title { position: absolute; left: 0; width: 1168px; top: 32px; text-align: center; }
  .care-list { position: absolute; left: 134px; top: 100px; width: 410px; list-style: none; }
  .care-item { position: absolute; left: 0; display: flex; gap: 10px; width: 410px; }
  .care-icon { flex: 0 0 64px; height: 64px; border-radius: 50%; background: #dcefe3; }
  .care-text { font-family: "Raleway", sans-serif; font-weight: 300; font-size: 12.5px; line-height: 22.4px; color: var(--body-ink); }
  .care-text a { color: var(--green); font-weight: 600; text-decoration: none; }

  .video-card { position: absolute; left: 587px; top: 103px; width: 373px; height: 336px; overflow: hidden;
    background: linear-gradient(160deg, #8a8070 0%, #cfc6b6 40%, #e8e2d8 60%, #7a7060 100%); }
  .video-band { position: absolute; left: 0; top: 24px; width: 373px; height: 98px; background: var(--green-band);
    padding: 22px 16px 0 20px; }
  .video-band p { font-weight: 700; font-size: 21px; line-height: 27px; color: var(--white); white-space: nowrap; }
  .play-button { position: absolute; left: 228px; top: 140px; }
</style>
</head>
<body>
  <header class="site-header">
    <div class="brand"><span class="brand-dot"></span><span class="brand-name">Put Your Logo Here</span></div>
    <nav class="main-nav">
      <a href="#" class="is-active">Home</a>
      <a href="#">Our Animal Sanctuary</a>
      <a href="#">Animal Protection</a>
      <a href="#">About Us</a>
    </nav>
  </header>

  <section class="hero" role="img" aria-label="Sheep grazing on a sunlit meadow among forest trees behind a wooden fence">
    <h1 class="hero-title">Animals Life Does Matter !</h1>
    <a class="hero-button" href="#">LEARN MORE</a>
  </section>

  <section class="vision">
    <h2 class="section-title">Our Vision.</h2>
    <p class="vision-text">Lorem ipsum dolor sit amet, consectetur adipisicing elit, sed do eiusmod tempor incididunt ut labore etdolore magna aliqua. Ut enim ad minim ve niam, quisnostrud exercitation ullamco laboris nisi ut aliquip ex ea comm odo consequat. Duis aute irure dolor in reprehen-derit in voluptate velit esse cillum dolore eu fugiat nulla &nbsp;pariatur. Excepteur sint occaecat cupid atat non proi-</p>
    <div class="vision-photo" role="img" aria-label="Close-up of a young white lamb"></div>
  </section>

  <section class="protection">
    <h2 class="section-title">Animal Protection</h2>
    <ul class="care-list">
      <li class="care-item" style="top:0">
        <span class="care-icon" role="img" aria-label="Green line icon of a hen"></span>
        <p class="care-text">Lorem ipsum dolor sit amet, consectetur adipisicing elit, sed do eiusmod tempor incididunt ut labore etdolore m agna aliqua. <a href="#">Read More...</a></p>
      </li>
      <li class="care-item" style="top:86px">
        <span class="care-icon" role="img" aria-label="Green line icon of a cow with a heart"></span>
        <p class="care-text">Lorem ipsum dolor sit amet, consectetur adipisicing elit, sed do eiusmod tempor incididunt ut labore etdolore m agna aliqua. <a href="#">Read More...</a></p>
      </li>
      <li class="care-item" style="top:166px">
        <span class="care-icon" role="img" aria-label="Green line icon of eggs in a nest"></span>
        <p class="care-text">Lorem ipsum dolor sit amet, consectetur adipisicing elit, sed do eiusmod tempor incididunt ut labore etdolore m agna aliqua. <a href="#">Read More...</a></p>
      </li>
      <li class="care-item" style="top:246px">
        <span class="care-icon" role="img" aria-label="Green line icon of a pig face"></span>
        <p class="care-text">Lorem ipsum dolor sit amet, consectetur adipisicing elit, sed do eiusmod tempor incididunt ut labore etdolore m agna aliqua. <a href="#">Read More...</a></p>
      </li>
    </ul>

    <div class="video-card" role="img" aria-label="Video still of a woolly sheep in a field">
      <div class="video-band"><p>Our vision is a world where<br>animals live free from suffering</p></div>
      <svg class="play-button" width="56" height="56" viewBox="0 0 56 56" aria-hidden="true">
        <circle cx="28" cy="28" r="28" fill="#f4f2f0" fill-opacity="0.92"/>
        <path d="M22 18 L38 28 L22 38 Z" fill="#6b6b6b"/>
      </svg>
    </div>
  </section>
</body>
</html>
```